Ferncrest Dental, LLC business card project

Business card to be designed with current logo.
Dental office- please keep design of card that looks clean and professional.
Please include the following info:
Ferncrest Dental, LLC
Dr. Lorna Pettigrew
2871 Marlowe Street
Bethlehem, PA 18093
610-555-0193
ferncrestdental.office@examplemail.test
Hello everyone-
Reason: Just got back from overseas- will look at all designs and provide feedback. Thank you!
Reason: Polling my friends for the final selection-
thank you to all those that participated- so many talented designers!

```html
<!DOCTYPE html>
<html lang="en">
<head>
<meta charset="utf-8">
<title>Ferncrest Dental – Appointment Card</title>
<link href="https://fonts.googleapis.com/css2?family=Arimo:wght@400&display=swap" rel="stylesheet">
<style>
  :root {
    --paper: #ffffff;
    --ink-soft: #bdbdbd;
    --ink-faint: #c4c4c4;
    --rule: #cfcfcf;
    --edge: #8a8a8a;
  }
  * { margin: 0; padding: 0; box-sizing: border-box; }
  html, body {
    width: 686px;
    height: 1200px;
    overflow: hidden;
    background: var(--paper);
  }
  .card {
    position: relative;
    width: 686px;
    height: 1200px;
    background: var(--paper);
    border: 1.5px solid var(--edge);
    font-family: "Arimo", Arial, sans-serif;
    color: var(--ink-soft);
  }
  .card__title {
    position: absolute;
    top: 22px;
    left: 0;
    width: 100%;
    text-align: center;
    font-size: 41px;
    font-weight: 400;
    letter-spacing: 0.5px;
  }
  .card__label {
    position: absolute;
    top: 96px;
    font-size: 38px;
    font-weight: 400;
  }
  .card__label--date { left: 34px; }
  .card__label--hour { left: 439px; }
  .schedule {
    position: absolute;
    top: 143px;
    left: 17px;
    width: 649px;
    height: 904px;
    border: 2px solid var(--rule);
    display: grid;
    grid-template-columns: 415px 1fr;
    grid-template-rows: repeat(10, 1fr);
  }
  .schedule__date,
  .schedule__hour {
    border-bottom: 2px solid var(--rule);
  }
  .schedule__date { border-right: 2px solid var(--rule); }
  .schedule__date:nth-last-child(2),
  .schedule__hour:last-child { border-bottom: none; }
  .schedule__hour {
    display: flex;
    flex-direction: column;
    justify-content: space-around;
    align-items: flex-end;
    padding: 4px 6px 2px 0;
    font-size: 25px;
    letter-spacing: 3px;
    color: var(--ink-faint);
    line-height: 1;
  }
  .card__phone {
    position: absolute;
    top: 1078px;
    left: 0;
    width: 100%;
    text-align: center;
    font-size: 51px;
    font-weight: 400;
    letter-spacing: 0.5px;
  }
</style>
</head>
<body>
  <div class="card">
    <h1 class="card__title">NEXT APPOINTMENT</h1>
    <div class="card__label card__label--date">DATE</div>
    <div class="card__label card__label--hour">HOUR</div>

    <div class="schedule">
      <div class="schedule__date"></div><div class="schedule__hour"><span>A.M.</span><span>P.M.</span></div>
      <div class="schedule__date"></div><div class="schedule__hour"><span>A.M.</span><span>P.M.</span></div>
      <div class="schedule__date"></div><div class="schedule__hour"><span>A.M.</span><span>P.M.</span></div>
      <div class="schedule__date"></div><div class="schedule__hour"><span>A.M.</span><span>P.M.</span></div>
      <div class="schedule__date"></div><div class="schedule__hour"><span>A.M.</span><span>P.M.</span></div>
      <div class="schedule__date"></div><div class="schedule__hour"><span>A.M.</span><span>P.M.</span></div>
      <div class="schedule__date"></div><div class="schedule__hour"><span>A.M.</span><span>P.M.</span></div>
      <div class="schedule__date"></div><div class="schedule__hour"><span>A.M.</span><span>P.M.</span></div>
      <div class="schedule__date"></div><div class="schedule__hour"><span>A.M.</span><span>P.M.</span></div>
      <div class="schedule__date"></div><div class="schedule__hour"><span>A.M.</span><span>P.M.</span></div>
    </div>

    <div class="card__phone">610-555-0193</div>
  </div>
</body>
</html>
```